Design Chinese text on the PSD banner template

Add Chinese text on the PSD banner template.
-delete all the current text on the template
-the design of the text must suite the template, prefer high end, luxury, gold metal effect.

main text:
批盘 90%

secondary text:
-真人 -电子 -捕鱼 -体育 -棋牌 -彩票
多达1200++种游戏

Banner PSD template download link:
https://qv.zx/t-RAPlWoUbtz

(the meaning of those Chinese text is:

Wholesale Game Credit 90%

-live game -slot game -fishing game -sports game -poker game -lottery game
more than 1200++ games )

```html
<!DOCTYPE html>
<html lang="zh">
<head>
<meta charset="utf-8">
<title>批盘 90% Banner</title>
<link href="https://fonts.googleapis.com/css2?family=Noto+Serif+SC:wght@900&family=Noto+Sans+SC:wght@700&family=Cinzel:wght@900&display=swap" rel="stylesheet">
<style>
  :root {
    --backdrop: #160608;
    --banner-deep: #1a0704;
    --banner-amber: #c0700e;
    --glow-gold: #ffc24a;
    --gold-light: #fff6c4;
    --gold-mid: #e8ae32;
    --gold-dark: #6e3e04;
    --gold-edge: #3a1c00;
    --text-cream: #ffe6b0;
    --stage-red: #c81c0a;
    --stage-glow: #ffa826;
  }
  * { margin: 0; padding: 0; box-sizing: border-box; }
  html, body { width: 1200px; height: 848px; overflow: hidden; background: var(--backdrop); }
  .canvas { position: relative; width: 1200px; height: 848px; background: var(--backdrop); }
  .banner { position: absolute; left: 247px; top: 27px; width: 706px; height: 789px; overflow: hidden; }
  .banner-backdrop {
    position: absolute; inset: 0;
    background:
      radial-gradient(ellipse 42% 9% at 50% 84%, rgba(255,178,50,.75), rgba(200,40,12,.55) 45%, transparent 100%),
      radial-gradient(ellipse 65% 16% at 50% 85%, rgba(200,28,10,.45), transparent 100%),
      radial-gradient(ellipse 40% 70% at 50% 0%, rgba(255,210,90,.85), rgba(230,150,40,.45) 50%, transparent 90%),
      radial-gradient(ellipse 90% 60% at 50% 30%, rgba(210,120,20,.6), transparent 85%),
      linear-gradient(180deg, var(--banner-amber) 0%, #8a420a 42%, #3a1406 64%, var(--banner-deep) 78%, #0c0302 100%);
  }
  .headline {
    position: absolute; left: 0; right: 0; top: 300px; text-align: center;
    font-family: "Noto Serif SC", serif; font-weight: 900; font-size: 122px; line-height: 1;
    letter-spacing: 4px; white-space: nowrap;
    background:
      repeating-linear-gradient(115deg, rgba(255,255,255,0) 0 7px, rgba(255,245,200,.35) 7px 9px, rgba(90,50,0,.25) 9px 12px),
      linear-gradient(180deg, var(--gold-light) 0%, #f7d36a 22%, var(--gold-mid) 40%, var(--gold-dark) 52%, #b57a18 62%, var(--gold-mid) 78%, var(--gold-light) 100%);
    -webkit-background-clip: text; background-clip: text; color: transparent;
    -webkit-text-stroke: 1.5px rgba(90,48,0,.9);
    filter:
      drop-shadow(0 -1px 0 rgba(255,248,210,.9))
      drop-shadow(1px 2px 0 var(--gold-edge))
      drop-shadow(0 4px 4px rgba(20,5,0,.85))
      drop-shadow(0 0 14px rgba(255,170,40,.45));
  }
  .headline .figure { font-family: "Cinzel", serif; font-size: 90px; margin-left: 52px; }
  .divider {
    position: absolute; left: 193px; top: 478px; width: 307px; height: 3px;
    background: linear-gradient(90deg, transparent, var(--gold-mid) 25%, #fff 50%, var(--gold-mid) 75%, transparent);
    box-shadow: 0 0 10px rgba(255,200,100,.8);
  }
  .categories, .game-count {
    position: absolute; left: 0; right: 0; text-align: center; white-space: nowrap;
    font-family: "Noto Sans SC", sans-serif; font-weight: 700; color: var(--text-cream);
    text-shadow: 0 2px 3px rgba(40,10,0,.9), 0 0 8px rgba(255,160,40,.5);
  }
  .categories { top: 500px; font-size: 34px; letter-spacing: 1px; }
  .game-count { top: 546px; font-size: 36px; }
</style>
</head>
<body>
<div class="canvas">
  <section class="banner">
    <div class="banner-backdrop" role="img" aria-label="Golden spotlight beams with falling sparkles over a glowing red stage floor"></div>
    <h1 class="headline">批盘<span class="figure">90%</span></h1>
    <div class="divider"></div>
    <p class="categories">-真人 -电子 -捕鱼 -体育 -棋牌 -彩票</p>
    <p class="game-count">多达1200++种游戏</p>
  </section>
</div>
</body>
</html>
```